BRISKFOLDER.US / logo winner announced
Need Business card + Stationery
Professional
Tavid P.Onsgard
President
Four Maple Court East suit 318 Dunmore Hill, NJ 07931
517-64-BRISK
Tavid@briskfolder.US
BriskFolder.US
Please check out Logo Winner (#46) Link: http://www.pixelquarry.com/contests/logo-bus-card-briskfolder-us and utilize this Logo into card and Stationery.
Up to Designer. You can make it a 2-sided card if you geel its better..

```html
<!DOCTYPE html>
<html lang="en">
<head>
<meta charset="utf-8">
<title>BriskFolder.US Stationery Concepts</title>
<link href="https://fonts.googleapis.com/css2?family=Open+Sans:wght@300;400;600;700&display=swap" rel="stylesheet">
<style>
  :root {
    --board: #1c1c1c;
    --board-light: #2a2a2a;
    --green: #5a9e2f;
    --green-dark: #3f7d1e;
    --blue: #1f6fa8;
    --blue-dark: #134f7e;
    --paper: #ffffff;
    --ink: #4a4a4a;
    --caption: #8a8a8a;
    --faint: #e6eef0;
  }
  * { margin: 0; padding: 0; box-sizing: border-box; }
  html, body { width: 1200px; height: 593px; overflow: hidden; background: var(--board); }
  .board {
    position: relative; width: 1200px; height: 593px;
    background: radial-gradient(ellipse at 50% 40%, var(--board-light), var(--board) 75%);
    font-family: "Open Sans", sans-serif;
  }
  .brand-mark { position: absolute; border-radius: 50%; background: var(--green); }
  .brand-name { font-family: "Open Sans", sans-serif; font-weight: 600; color: var(--green); white-space: nowrap; }
  .caption { position: absolute; color: var(--caption); font-size: 9px; text-align: center; }

  .intro { position: absolute; left: 30px; top: 90px; width: 250px; text-align: center; }
  .intro .brand-mark { position: static; display: block; width: 46px; height: 46px; margin: 0 auto 22px; }
  .intro .brand-name { font-size: 26px; }
  .intro .subtitle { color: var(--caption); font-size: 13px; font-weight: 300; margin-top: 10px; letter-spacing: 0.5px; }

  .card {
    position: absolute; left: 38px; top: 236px; width: 232px; height: 128px;
    background: var(--paper); border-radius: 5px; overflow: hidden;
  }
  .card .brand-mark { left: 102px; top: 8px; width: 28px; height: 28px; }
  .card .brand-name { position: absolute; left: 0; width: 100%; top: 39px; text-align: center; font-size: 13px; }
  .card .band { position: absolute; left: 0; top: 58px; }
  .card .person { position: absolute; left: 10px; top: 80px; color: #fff; font-size: 7.5px; line-height: 1.3; width: 110px; }
  .card .person strong { font-size: 8.5px; display: block; }
  .card .person small { font-size: 5.5px; display: block; margin-top: 3px; line-height: 1.35; }
  .card .contacts { position: absolute; left: 128px; top: 78px; list-style: none; color: #fff; font-size: 6px; line-height: 11px; }
  .card .contacts li { display: flex; align-items: center; gap: 4px; }
  .card .contacts svg { width: 7px; height: 7px; flex: none; }

  .letterhead {
    position: absolute; left: 288px; top: 34px; width: 384px; height: 499px;
    background: var(--paper); overflow: hidden;
  }
  .letterhead .brand-mark { left: 62px; top: 14px; width: 36px; height: 36px; }
  .letterhead .brand-name { position: absolute; left: 12px; top: 54px; font-size: 14px; }
  .letterhead .address { position: absolute; left: 276px; top: 10px; font-size: 6px; line-height: 9.5px; color: var(--ink); font-style: normal; }
  .letterhead .faint-circle { position: absolute; left: 108px; top: 190px; width: 168px; height: 168px; border-radius: 50%; background: var(--faint); }
  .letterhead .footer-wave { position: absolute; left: 0; bottom: 0; }

  .envelopes { position: absolute; left: 684px; top: 90px; }
  .env-front-mark { position: absolute; left: 750px; top: 360px; width: 28px; height: 28px; }
  .env-front-text { position: absolute; left: 698px; top: 394px; }
  .env-front-text .brand-name { font-size: 12px; }
  .env-front-text .address { font-size: 5.5px; color: var(--ink); line-height: 8px; margin-top: 3px; }
</style>
</head>
<body>
<main class="board">

  <section class="intro">
    <span class="brand-mark"></span>
    <div class="brand-name">BRISKFOLDER.US</div>
    <p class="subtitle">Stationery Concepts</p>
  </section>

  <article class="card">
    <span class="brand-mark"></span>
    <div class="brand-name">BriskFolder.US</div>
    <svg class="band" width="232" height="70" viewBox="0 0 232 70">
      <defs>
        <linearGradient id="cardGreen" x1="0" y1="0" x2="1" y2="1">
          <stop offset="0" stop-color="#6fb23a"/><stop offset="1" stop-color="#2f6d17"/>
        </linearGradient>
      </defs>
      <path d="M0 10 C80 0 150 0 232 12 L232 70 L0 70 Z" fill="var(--blue)"/>
      <path d="M0 16 C80 6 150 6 232 18 L232 70 L0 70 Z" fill="url(#cardGreen)"/>
    </svg>
    <div class="person">
      <strong>Tavid P.Onsgard</strong>
      President
      <small>Four Maple Court East suit 318<br>Dunmore Hill, NJ 07931</small>
    </div>
    <ul class="contacts">
      <li><svg viewBox="0 0 8 8"><path d="M1 1h2l1 2-1 1a4 4 0 0 0 1 1l1-1 2 1v2h-1A6 6 0 0 1 1 2Z" fill="#fff"/></svg>517-64-BRISK</li>
      <li><svg viewBox="0 0 8 8"><rect x="0.5" y="1.5" width="7" height="5" fill="none" stroke="#fff"/><path d="M0.5 1.5 4 4.5 7.5 1.5" fill="none" stroke="#fff"/></svg>Tavid@briskfolder.US</li>
      <li><svg viewBox="0 0 8 8"><circle cx="4" cy="4" r="3.3" fill="none" stroke="#fff"/><path d="M0.7 4h6.6M4 0.7v6.6" stroke="#fff" stroke-width="0.7"/></svg>BriskFolder.US</li>
      <li><svg viewBox="0 0 8 8"><path d="M4 7.6S1.2 4.6 1.2 3a2.8 2.8 0 0 1 5.6 0C6.8 4.6 4 7.6 4 7.6Z" fill="#fff"/></svg>briskfolder-us</li>
    </ul>
  </article>
  <p class="caption" style="left:38px; top:370px; width:232px;">Business Card Design</p>

  <article class="letterhead">
    <span class="brand-mark"></span>
    <div class="brand-name">BriskFolder.US</div>
    <address class="address">
      Four Maple Court East<br>suit 318<br>Dunmore Hill, NJ 07931<br>517-64-BRISK<br>Tavid@briskfolder.US<br>BriskFolder.US
    </address>
    <span class="faint-circle"></span>
    <svg class="footer-wave" width="384" height="40" viewBox="0 0 384 40">
      <path d="M0 14 C120 2 260 2 384 18 L384 40 L0 40 Z" fill="var(--blue)"/>
      <path d="M0 24 C130 10 260 12 384 26 L384 40 L0 40 Z" fill="var(--green)"/>
      <path d="M0 32 C130 20 260 22 384 34 L384 40 L0 40 Z" fill="var(--paper)"/>
    </svg>
  </article>
  <p class="caption" style="left:288px; top:542px; width:384px;">Letterhead</p>

  <svg class="envelopes" width="400" height="450" viewBox="0 0 400 450">
    <defs>
      <linearGradient id="flapBlue" x1="0" y1="0" x2="0" y2="1">
        <stop offset="0" stop-color="#2a86c4"/><stop offset="1" stop-color="var(--blue-dark)"/>
      </linearGradient>
      <linearGradient id="flapGreen" x1="0" y1="0" x2="0" y2="1">
        <stop offset="0" stop-color="#7cc043"/><stop offset="1" stop-color="var(--green-dark)"/>
      </linearGradient>
    </defs>
    <g class="envelope envelope-back" transform="rotate(9 200 100)">
      <rect x="20" y="10" width="365" height="170" fill="var(--paper)"/>
      <path d="M20 10 L200 85 L385 10 Z" fill="url(#flapBlue)"/>
      <circle cx="330" cy="40" r="11" fill="var(--green)"/>
    </g>
    <g class="envelope envelope-middle" transform="rotate(5 200 160)">
      <rect x="12" y="70" width="375" height="170" fill="var(--paper)"/>
      <path d="M12 70 L200 140 L387 70 Z" fill="url(#flapGreen)"/>
      <circle cx="350" cy="125" r="10" fill="var(--green)"/>
    </g>
    <g class="envelope envelope-front">
      <path d="M5 222 L190 185 L384 222 Z" fill="var(--paper)"/>
      <rect x="5" y="222" width="379" height="221" fill="var(--paper)"/>
      <path d="M5 222 L190 280 L384 222" fill="none" stroke="#dcdcdc"/>
      <circle cx="324" cy="342" r="58" fill="var(--faint)"/>
    </g>
  </svg>
  <span class="brand-mark env-front-mark"></span>
  <div class="env-front-text">
    <div class="brand-name">BriskFolder.US</div>
    <p class="address">Four Maple Court East suit 318<br>Dunmore Hill, NJ 07931</p>
  </div>
  <p class="caption" style="left:689px; top:542px; width:379px;">Envelope</p>

</main>
</body>
</html>
```